Billboard Design for Equipment Rental Business

We need a billboard design for our equipment rental business called Brevard Machinery Company. We are based in Georgia. We rent construction tools, equipment, and dumpsters. We currently have a design but feel like we could get something better. Our phone number is 912-307-5186 and our website is www.brevardmachinery-example.com

```html
<!DOCTYPE html>
<html lang="en">
<head>
<meta charset="UTF-8">
<title>Brevard Machinery Company Billboard</title>
<link rel="stylesheet" href="https://fonts.googleapis.com/css2?family=Barlow:wght@700&family=Bebas+Neue&display=swap">
<style>
  :root {
    --ink: #0d0d0d;
    --safety-yellow: #f8bf2a;
    --yellow-shade: #efb524;
    --white: #ffffff;
  }
  html, body {
    margin: 0;
    padding: 0;
    width: 1200px;
    height: 675px;
    overflow: hidden;
    background: var(--ink);
  }
  .billboard {
    position: relative;
    width: 1200px;
    height: 675px;
    background: var(--ink);
    overflow: hidden;
  }
  .panel-shape {
    position: absolute;
    inset: 0;
  }
  .machine-art {
    position: absolute;
    left: 116px;
    top: 78px;
    width: 326px;
    height: 242px;
    border-radius: 10px;
    background: var(--yellow-shade);
  }
  .brand-name {
    position: absolute;
    left: 60px;
    top: 322px;
    width: 486px;
    margin: 0;
    text-align: center;
    font-family: "Barlow", sans-serif;
    font-weight: 700;
    color: var(--ink);
    line-height: 1;
  }
  .brand-name .brand-main {
    display: block;
    font-size: 112px;
    letter-spacing: 2px;
  }
  .brand-name .brand-sub {
    display: block;
    margin-top: 12px;
    font-size: 36px;
    letter-spacing: 4px;
  }
  .services {
    position: absolute;
    left: 614px;
    top: 92px;
    margin: 0;
    padding: 0;
    list-style: none;
    font-family: "Bebas Neue", sans-serif;
    font-size: 122px;
    line-height: 120px;
    color: var(--ink);
  }
  .services li {
    display: flex;
    align-items: center;
    height: 120px;
  }
  .services .bullet {
    width: 34px;
    height: 34px;
    margin: 0 38px 12px 0;
    background: var(--ink);
    transform: rotate(45deg);
    flex: none;
  }
  .phone {
    position: absolute;
    left: 566px;
    top: 518px;
    margin: 0;
    font-family: "Bebas Neue", sans-serif;
    font-size: 117px;
    line-height: 1;
    letter-spacing: 2px;
    color: var(--safety-yellow);
  }
  .website {
    position: absolute;
    left: 52px;
    top: 586px;
    width: 480px;
    margin: 0;
    white-space: nowrap;
    font-family: "Bebas Neue", sans-serif;
    font-size: 35px;
    line-height: 1;
    color: var(--safety-yellow);
  }
  .website .web-accent {
    color: var(--white);
  }
</style>
</head>
<body>
  <main class="billboard">
    <svg class="panel-shape" width="1200" height="675" viewBox="0 0 1200 675" aria-hidden="true">
      <path fill="var(--safety-yellow)" d="M31 25 H1168 V500 H566 C540 500 526 512 516 528 C506 544 494 553 470 553 H31 Z"/>
    </svg>

    <div class="machine-art" role="img" aria-label="Line illustration of an excavator with bucket arm and tracks"></div>

    <h1 class="brand-name">
      <span class="brand-main">BREVARD</span>
      <span class="brand-sub">MACHINERY COMPANY</span>
    </h1>

    <ul class="services">
      <li><span class="bullet"></span>Tools</li>
      <li><span class="bullet"></span>Equipment</li>
      <li><span class="bullet"></span>Dumpsters</li>
    </ul>

    <p class="website">WWW.BREVARD<span class="web-accent">MACHINERY-EXAMPLE</span>.COM</p>

    <p class="phone">912-307-5186</p>
  </main>
</body>
</html>
```